Washington DC Solo Practitioner Law Firm needs Stationery and Business Card Design

We need a letterhead and business card for a new law firm based in Washington DC called Marlowe PLLC. The law firm is a single lawyer practicing appellate law (U.S. Supreme Court, Federal District Courts, State Supreme Courts).
We already have a logo designed through a PixelBazaar contest. The letterhead and the business card should include the Logo and have the same look and feel as the Logo - same fonts and colors, please. We would like a clean, crisp, simple, professional look. The design should convey stability and experience.
We have .png and .psd and .ai files for the logo, as needed
Dark blue color is PANTONE P 108-16 C
Grey color is PANTONE P 179-11 C
Type face is Century Gothic Regular typeface

```html
<!DOCTYPE html>
<html lang="en">
<head>
<meta charset="utf-8">
<title>Marlowe PLLC — Letterhead</title>
<link rel="stylesheet" href="https://fonts.googleapis.com/css2?family=Didact+Gothic&display=swap">
<style>
  :root {
    --backdrop: #d0d0d0;
    --paper: #f4f4f4;
    --navy: #1d3557;
    --grey-mark: #d6dae1;
    --footer-ink: #5a6270;
  }
  * { margin: 0; padding: 0; box-sizing: border-box; }
  html, body {
    width: 1200px;
    height: 931px;
    overflow: hidden;
    background: var(--backdrop);
  }
  body {
    font-family: "Didact Gothic", "Century Gothic", sans-serif;
    display: flex;
    align-items: center;
    justify-content: center;
  }
  .letterhead {
    position: relative;
    width: 640px;
    height: 828px;
    background: var(--paper);
    box-shadow: 0 2px 10px rgba(0, 0, 0, 0.08);
  }
  .brand {
    position: absolute;
    top: 64px;
    left: 50%;
    transform: translateX(-50%);
    display: flex;
    align-items: center;
    gap: 12px;
    color: var(--navy);
  }
  .brand-square {
    width: 30px;
    height: 30px;
    background: var(--navy);
  }
  .brand-text {
    display: flex;
    flex-direction: column;
    line-height: 1;
  }
  .brand-name {
    font-size: 26px;
    letter-spacing: 1px;
  }
  .brand-suffix {
    font-size: 13px;
    letter-spacing: 6px;
    margin-top: 3px;
    text-align: center;
  }
  .brand-tagline {
    font-size: 7px;
    letter-spacing: 1px;
    margin-top: 5px;
  }
  .watermark {
    position: absolute;
    top: 50%;
    left: 50%;
    width: 150px;
    height: 150px;
    transform: translate(-50%, -50%);
    background: var(--grey-mark);
  }
  .footer-contact {
    position: absolute;
    left: 56px;
    bottom: 40px;
    font-size: 8.5px;
    letter-spacing: 0.3px;
    color: var(--footer-ink);
  }
  .footer-contact .sep { margin: 0 6px; }
</style>
</head>
<body>
  <main class="letterhead">
    <header class="brand">
      <span class="brand-square"></span>
      <div class="brand-text">
        <span class="brand-name">MARLOWE</span>
        <span class="brand-suffix">PLLC</span>
        <span class="brand-tagline">TRIAL AND APPELLATE LITIGATION</span>
      </div>
    </header>

    <div class="watermark" aria-hidden="true"></div>

    <footer class="footer-contact">
      1820 L Street NW, Suite 400, Washington, DC 20036<span class="sep">|</span>202-555-0148<span class="sep">|</span>571-555-0192
    </footer>
  </main>
</body>
</html>
```